Business Cards and Stationary for a new consulting, recruiting and outsourcing company in Germany
BRAUNFELD Consulting
Business Cards and Stationary for a new consulting, recruiting and outsourcing company in Germany  - Consulting
Creative Brief
Professional
BRAUNFELD Consulting (Company Name) Ramune Braunfeld (First name, last name)
Inhaberin ("Owner" for english version)
Im Lindgrund 5 89512 Tannbach Deutschland ("Germany" for english version)
ramune.braunfeld@braunfeld-beratung.example
htttps://www.braunfeld-beratung.example
The round logo version with black background size around 75% of the card.

```html
<!DOCTYPE html>
<html lang="en">
<head>
<meta charset="utf-8">
<title>BRAUNFELD Consulting – Stationery</title>
<link href="https://fonts.googleapis.com/css2?family=Open+Sans:wght@400;600;700&display=swap" rel="stylesheet">
<style>
  :root {
    --bg: #e9eaec;
    --paper: #ffffff;
    --blue: #22b0f0;
    --band: #d9dadc;
    --ink: #3a3a3a;
    --body: #555555;
    --accent: #f7941d;
    --black: #111111;
  }
  html, body {
    margin: 0; padding: 0;
    width: 1200px; height: 936px;
    overflow: hidden;
    background: var(--bg);
    font-family: "Open Sans", Arial, sans-serif;
    color: var(--ink);
  }
  .canvas { position: relative; width: 1200px; height: 936px; }
  .sheet { position: absolute; background: var(--paper); overflow: hidden; }

  /* brand block: plain name with one dot */
  .brand { display: flex; align-items: center; gap: 8px; }
  .brand-dot { border-radius: 50%; background: var(--blue); flex: none; }
  .brand-name { font-weight: 600; color: var(--ink); white-space: nowrap; }

  /* letterhead */
  .letterhead { left: 177px; top: 51px; width: 443px; height: 569px; }
  .letterhead .brand { position: absolute; left: 28px; top: 28px; }
  .letterhead .brand-dot { width: 22px; height: 22px; }
  .letterhead .brand-name { font-size: 14px; }
  .letter-body { position: absolute; left: 40px; top: 100px; width: 330px; font-size: 6.5px; line-height: 1.55; color: var(--body); }
  .letter-body p { margin: 0 0 9px; }
  .letter-meta p { margin: 0; }
  .signature { width: 40px; height: 14px; background: linear-gradient(90deg, #4a4a4a, #7a7a7a); border-radius: 3px; margin: 4px 0; opacity: .7; }
  .letter-footer { position: absolute; left: 0; bottom: 6px; width: 100%; height: 22px; background: var(--blue);
    display: flex; align-items: center; justify-content: space-around; font-size: 6px; color: #fff; }
  .letter-footer span { display: flex; align-items: center; gap: 4px; }
  .letter-footer svg { width: 8px; height: 8px; }
  .letter-accent { position: absolute; left: 0; bottom: 0; width: 100%; height: 6px; background: var(--accent); }

  /* folder */
  .folder { left: 632px; top: 51px; width: 431px; height: 569px; background: var(--blue); }
  .folder-band { position: absolute; left: 0; top: 212px; width: 100%; height: 156px; background: var(--band); }
  .folder-band-inner { position: absolute; left: 0; top: 14px; width: 100%; height: 128px; background: var(--paper);
    display: flex; align-items: center; justify-content: center; }
  .folder .brand { gap: 12px; }
  .folder .brand-dot { width: 44px; height: 44px; }
  .folder .brand-name { font-size: 22px; }
  .folder-web { position: absolute; left: 26px; bottom: 22px; font-size: 10px; color: #fff; letter-spacing: .12em; }

  /* business cards */
  .card { left: 71px; width: 169px; height: 106px; }
  .card-front { top: 658px; }
  .card-front .brand { position: absolute; left: 10px; top: 10px; gap: 5px; }
  .card-front .brand-dot { width: 12px; height: 12px; }
  .card-front .brand-name { font-size: 8px; }
  .card-person { position: absolute; left: 10px; top: 36px; font-size: 5.5px; line-height: 1.4; }
  .card-person strong { font-size: 6.5px; color: var(--ink); }
  .card-strip { position: absolute; left: 0; bottom: 0; width: 100%; height: 30px; background: var(--blue); color: #fff;
    font-size: 4.6px; line-height: 1.45; padding: 4px 10px; box-sizing: border-box; }
  .card-back { top: 785px; background: var(--black); display: flex; align-items: center; justify-content: center; }
  .card-back .brand-dot { width: 20px; height: 20px; }
  .card-back .brand-name { font-size: 10.5px; color: #fff; }

  /* envelope front */
  .envelope-front { left: 266px; top: 747px; width: 468px; height: 151px; }
  .envelope-front .brand { position: absolute; left: 18px; top: 18px; }
  .envelope-front .brand-dot { width: 20px; height: 20px; }
  .envelope-front .brand-name { font-size: 13px; }
  .envelope-strip { position: absolute; left: 0; bottom: 18px; width: 100%; height: 16px; background: var(--blue);
    color: #fff; font-size: 7px; letter-spacing: .14em; display: flex; align-items: center; padding-left: 110px; box-sizing: border-box; }

  /* envelope back */
  .envelope-back { left: 759px; top: 747px; width: 354px; height: 151px; }
  .envelope-flap { position: absolute; left: 0; top: 0; width: 100%; height: 62px; }
  .envelope-web { position: absolute; left: 0; top: 12px; width: 100%; text-align: center; color: #fff; font-size: 7px; letter-spacing: .14em; }
</style>
</head>
<body>
<div class="canvas">

  <section class="sheet letterhead">
    <div class="brand">
      <span class="brand-dot"></span>
      <span class="brand-name">BRAUNFELD Consulting</span>
    </div>
    <div class="letter-body">
      <div class="letter-meta">
        <p>10 May 2024</p>
        <p>&nbsp;</p>
        <p>Recipient Name</p>
        <p>Company Street 12</p>
        <p>10115 City, Germany</p>
        <p>&nbsp;</p>
      </div>
      <p>Dear Sir or Madam,</p>
      <p>Thank you for your interest in our consulting, recruiting and outsourcing services. We help growing companies find the right people, shape lean processes and deliver projects with clarity, care and measurable results.</p>
      <p>Our team works closely with you from the first talk to the final handover. Each step is planned, documented and reviewed so you always know where your project stands.</p>
      <p>We look forward to meeting you and discussing how we can support your goals this year.</p>
      <p>Kind regards,</p>
      <div class="signature" role="img" aria-label="Handwritten signature"></div>
      <div class="letter-meta">
        <p>Ramune Braunfeld</p>
        <p>Inhaberin</p>
        <p>Im Lindgrund 5, 89512 Tannbach</p>
      </div>
    </div>
    <div class="letter-footer">
      <span><svg viewBox="0 0 10 10"><path d="M5 0.5a3.3 3.3 0 0 0-3.3 3.3C1.7 6.4 5 9.5 5 9.5s3.3-3.1 3.3-5.7A3.3 3.3 0 0 0 5 0.5z" fill="#fff"/></svg>Im Lindgrund 5, 89512 Tannbach</span>
      <span><svg viewBox="0 0 10 10"><rect x="0.5" y="2" width="9" height="6" fill="none" stroke="#fff"/><path d="M0.5 2l4.5 3.5L9.5 2" fill="none" stroke="#fff"/></svg>ramune.braunfeld@braunfeld-beratung.example</span>
      <span><svg viewBox="0 0 10 10"><circle cx="5" cy="5" r="4.3" fill="none" stroke="#fff"/><path d="M0.7 5h8.6M5 0.7c2.4 2.6 2.4 6 0 8.6M5 0.7c-2.4 2.6-2.4 6 0 8.6" fill="none" stroke="#fff" stroke-width=".7"/></svg>www.braunfeld-beratung.example</span>
    </div>
    <div class="letter-accent"></div>
  </section>

  <section class="sheet folder">
    <div class="folder-band">
      <div class="folder-band-inner">
        <div class="brand">
          <span class="brand-dot"></span>
          <span class="brand-name">BRAUNFELD Consulting</span>
        </div>
      </div>
    </div>
    <div class="folder-web">www.braunfeld-beratung.example</div>
  </section>

  <section class="sheet card card-front">
    <div class="brand">
      <span class="brand-dot"></span>
      <span class="brand-name">BRAUNFELD Consulting</span>
    </div>
    <div class="card-person">
      <strong>Ramune Braunfeld</strong><br>Inhaberin
    </div>
    <div class="card-strip">
      Im Lindgrund 5, 89512 Tannbach, Deutschland<br>
      ramune.braunfeld@braunfeld-beratung.example<br>
      htttps://www.braunfeld-beratung.example
    </div>
  </section>

  <section class="sheet card card-back">
    <div class="brand">
      <span class="brand-dot"></span>
      <span class="brand-name">BRAUNFELD Consulting</span>
    </div>
  </section>

  <section class="sheet envelope-front">
    <div class="brand">
      <span class="brand-dot"></span>
      <span class="brand-name">BRAUNFELD Consulting</span>
    </div>
    <div class="envelope-strip">www.braunfeld-beratung.example</div>
  </section>

  <section class="sheet envelope-back">
    <svg class="envelope-flap" viewBox="0 0 354 62" preserveAspectRatio="none">
      <path d="M0 0H354V30Q177 70 0 30Z" fill="var(--blue)"/>
    </svg>
    <div class="envelope-web">www.braunfeld-beratung.example</div>
  </section>

</div>
</body>
</html>
```